RZO Design tag

Looking to design a tag for our new hat & glove brand RZO Design. These are winter hats & gloves. Long story short these are lower cost/retail items but I'm trying to convey higher quality goods through a nice tag. I’ve attached a tag of another brand we have to give you a general idea of what I’d be looking for- but again for our new brand RZO Design.
I’m thinking we can do one general design- and then do it in 4 different color schemes: First one mimicking the attachment’s colors for ladies items- so a few different shades of pink. Then 2nd color scheme a darker more masculine color tone for mens or unisex items- maybe blue/dark blue, and then a 3rd color scheme for kids items that is more vibrant/kid like colors. Last one red & green for some Christmas items we do.
A few things:
• Trying to make the tags look classy as possible
• The tag will need to measure 2.25” high x 2” wide. The top little bit would have to be space left blank for a hole punch- just like on the attached sample tag. But again the tags designed would need to be 2.25" tall x 2" wide so not the same shape as the sample tag.
• For item name you can just put “Knit Hat” for the generic tag item name (in place of what says on the same “Chenille Slipper Bootie”). Please try to keep the writing a nice font similar to what is on this tag- again trying to have a classy tag look
• On the bottom center (In place of Made in China) it would just need to say “One Size” in standard font
Hope this helps & thank you
Target Market(s)
People buying winter hats & gloves
Industry/Entity Type
Retail- winter hats & gloves
Look and feel

```html
<!DOCTYPE html>
<html lang="en">
<head>
<meta charset="UTF-8">
<title>Knit Hat Tag Options</title>
<link rel="stylesheet" href="https://fonts.googleapis.com/css2?family=Pinyon+Script&family=Rajdhani:wght@700&display=swap">
<style>
  :root {
    --sun: #ffcc00;
    --paper: #ffffff;
    --tag-black: #000000;
    --gold: #ffcc00;
    --ray: #6b5300;
    --hole: #ffffff;
  }
  * { margin: 0; padding: 0; box-sizing: border-box; }
  html, body { width: 841px; height: 1200px; overflow: hidden; }
  body { position: relative; background: var(--paper); }

  .band { position: absolute; left: 0; width: 841px; height: 400px; }
  .band--sun { background: var(--sun); }
  .band--paper { background: var(--paper); }
  .band--top { top: 0; }
  .band--middle { top: 400px; }
  .band--bottom { top: 800px; }

  .tag {
    position: absolute;
    left: 321px;
    top: 88px;
    width: 199px;
    height: 224px;
    background: var(--tag-black);
    box-shadow: 18px 18px 2px rgba(0, 0, 0, 0.38);
  }
  .tag--rounded { border-radius: 19px; }
  .tag__art { position: absolute; inset: 0; width: 199px; height: 224px; display: block; }

  .tag__name {
    position: absolute;
    left: 0; right: 0;
    top: 88px;
    text-align: center;
    font-family: "Pinyon Script", cursive;
    font-size: 37px;
    line-height: 48px;
    color: var(--gold);
    white-space: nowrap;
  }
  .tag__size {
    position: absolute;
    left: 0; right: 0;
    top: 188px;
    text-align: center;
    font-family: "Rajdhani", sans-serif;
    font-weight: 700;
    font-size: 12px;
    line-height: 14px;
    letter-spacing: 0.2px;
    color: var(--gold);
  }
  .frame { fill: none; stroke: var(--gold); stroke-width: 1.2; }
  .hole { fill: var(--hole); }
</style>
</head>
<body>
  <div class="band band--sun band--top">
    <div class="tag">
      <svg class="tag__art" viewBox="0 0 199 224">
        <defs>
          <radialGradient id="glow-a" cx="50%" cy="50%" r="55%">
            <stop offset="0" stop-color="var(--ray)" stop-opacity="0.75"/>
            <stop offset="1" stop-color="var(--tag-black)" stop-opacity="0"/>
          </radialGradient>
        </defs>
        <rect x="14" y="14" width="171" height="196" fill="url(#glow-a)" role="img" aria-label="Fine gold sunburst rays radiating from the product name"/>
        <rect class="frame" x="11" y="12" width="177" height="200"/>
        <circle class="hole" cx="99.5" cy="23" r="7"/>
      </svg>
      <div class="tag__name">Knit Hat</div>
      <div class="tag__size">ONE SIZE</div>
    </div>
  </div>

  <div class="band band--paper band--middle">
    <div class="tag">
      <svg class="tag__art" viewBox="0 0 199 224">
        <defs>
          <radialGradient id="glow-b" cx="50%" cy="50%" r="55%">
            <stop offset="0" stop-color="var(--ray)" stop-opacity="0.75"/>
            <stop offset="1" stop-color="var(--tag-black)" stop-opacity="0"/>
          </radialGradient>
        </defs>
        <rect x="14" y="14" width="171" height="196" fill="url(#glow-b)" role="img" aria-label="Fine gold sunburst rays radiating from the product name"/>
        <path class="frame" d="M26,12 H173 A16,16 0 0 0 189,28 V197 A16,16 0 0 0 173,213 H26 A16,16 0 0 0 10,197 V28 A16,16 0 0 0 26,12 Z"/>
        <circle class="hole" cx="99.5" cy="23" r="7"/>
      </svg>
      <div class="tag__name">Knit Hat</div>
      <div class="tag__size">ONE SIZE</div>
    </div>
  </div>

  <div class="band band--sun band--bottom">
    <div class="tag tag--rounded">
      <svg class="tag__art" viewBox="0 0 199 224">
        <defs>
          <radialGradient id="glow-c" cx="50%" cy="50%" r="55%">
            <stop offset="0" stop-color="var(--ray)" stop-opacity="0.75"/>
            <stop offset="1" stop-color="var(--tag-black)" stop-opacity="0"/>
          </radialGradient>
        </defs>
        <rect x="14" y="14" width="171" height="196" fill="url(#glow-c)" role="img" aria-label="Fine gold sunburst rays radiating from the product name"/>
        <path class="frame" d="M26,12 H173 A16,16 0 0 0 189,28 V197 A16,16 0 0 0 173,213 H26 A16,16 0 0 0 10,197 V28 A16,16 0 0 0 26,12 Z"/>
        <circle class="hole" cx="99.5" cy="23" r="7"/>
      </svg>
      <div class="tag__name">Knit Hat</div>
      <div class="tag__size">ONE SIZE</div>
    </div>
  </div>
</body>
</html>
```